MOR

We need to design a power point presentation that can englobe all our company products.

This presentation has to have all the required to be used as template for future presentations.

We focus on prodcut developing for supermarkets, ( we help them with their own brand products ex. Sunny Pantry, KT, etc.)
Also we are on the marine industry, we develop ships and oil rigs for the Oil and deep water market.

Target Market(s)

Oil Companies
Supermarket companies
Retail Companies

Industry/Entity Type

It Company

Requirements
Must have
• Our Logo and company colors
Nice to have
• Something describing globalization.
Should not have
• Orange color

```html
<!DOCTYPE html>
<html lang="es">
<head>
<meta charset="utf-8">
<title>Strategic Review 2014 – Navara Marine Solutions</title>
<link href="https://fonts.googleapis.com/css2?family=Open+Sans:wght@300;400;600;700&display=swap" rel="stylesheet">
<style>
:root{
  --page:#e6e6e6;
  --slide:#f4f4f4;
  --white:#ffffff;
  --navy:#1d3a6e;
  --blue:#1fa3e0;
  --sky:#5cc6f2;
  --pale:#cfeefc;
  --green:#7cc242;
  --ink:#333a44;
  --rule:#7fc8ee;
  --cell:#e3f2fb;
}
*{margin:0;padding:0;box-sizing:border-box}
html,body{width:1200px;height:2671px;overflow:hidden;background:var(--page);font-family:"Open Sans",Arial,sans-serif;color:var(--ink)}
.slide{position:absolute;left:32px;width:1136px;height:852px;background:var(--slide);overflow:hidden;box-shadow:0 1px 4px rgba(0,0,0,.18)}
.slide--cover{top:32px;background:var(--white)}
.slide--products{top:911px}
.slide--company{top:1787px}
.art{position:absolute;left:0;top:0;width:1136px;height:852px}
.cover-title{position:absolute;left:82px;top:690px;font-size:41px;font-weight:300;color:var(--navy);letter-spacing:.5px}
.cover-title b{color:var(--blue);font-weight:700;font-size:32px;margin-left:6px}
.cover-sub{position:absolute;left:84px;top:744px;font-size:21px;font-weight:400;color:#666}
.brand{position:absolute;text-align:center;color:var(--navy);font-weight:400;line-height:1.05}
.brand .mark{display:block;margin:0 auto 8px;border-radius:50%;background:var(--navy)}
.brand--cover{left:900px;top:690px;width:240px;font-size:30px}
.brand--cover .mark{width:44px;height:44px}
.brand--cover small{display:block;font-size:18px}
.brand--foot{left:14px;top:742px;width:110px;font-size:20px}
.brand--foot .mark{width:28px;height:28px}
.brand--foot small{display:block;font-size:11px}
.head{position:absolute;left:40px;top:30px;width:1056px;height:48px;border-bottom:2px solid var(--rule)}
.head h1{position:absolute;left:0;bottom:6px;font-size:37px;font-weight:300;color:var(--navy)}
.head .tag{position:absolute;right:0;bottom:8px;font-size:20px;font-weight:400;color:var(--green)}
.head .tag b{color:var(--blue);font-weight:700}
.section-title{position:absolute;left:40px;font-size:22px;font-weight:400;color:var(--blue);text-transform:uppercase}
.section-title b{color:var(--navy);font-weight:700}
.products-title{top:130px;color:#2aa6e0}
.products-title b{color:var(--blue)}
.dims{position:absolute;left:46px;top:167px;font-size:13px;font-weight:700;color:var(--ink)}
.specs{position:absolute;top:214px;border-collapse:collapse;font-size:10.5px;text-transform:uppercase}
.specs td{height:24px;border-top:1.5px solid var(--rule);padding:0 4px;white-space:nowrap}
.specs tr:last-child td{border-bottom:1.5px solid var(--rule)}
.specs td.val{text-align:right;font-weight:700;background:linear-gradient(90deg,var(--cell),#f9fcfe)}
.specs--left{left:40px;width:303px}
.specs--left td.val{width:110px}
.specs--right{left:409px;width:320px}
.specs--right td.val{width:120px}
.lead{position:absolute;left:42px;top:158px;width:1060px;font-size:23px;line-height:1.38;font-weight:400;color:var(--blue);text-transform:uppercase}
.lead b{color:var(--blue);font-weight:700}
.body{position:absolute;left:42px;width:1060px;font-size:18px;line-height:1.42;color:var(--ink)}
.body b{font-weight:700;color:#111}
.body--one{top:282px}
.divider{position:absolute;left:42px;top:400px;width:390px;border-top:1.5px solid #bbb}
.company-title{top:440px;font-size:23px}
.company-title b{color:var(--blue)}
.body--two{top:490px}
</style>
</head>
<body>

<section class="slide slide--cover">
  <svg class="art" viewBox="0 0 1136 852" aria-hidden="true">
    <defs>
      <linearGradient id="sky" x1="0" y1="0" x2="0" y2="1">
        <stop offset="0" stop-color="#1a9ee0"/><stop offset=".6" stop-color="#6fcdf4"/><stop offset="1" stop-color="#ffffff"/>
      </linearGradient>
      <linearGradient id="band" x1="0" y1="0" x2="1" y2="0">
        <stop offset="0" stop-color="#ffffff" stop-opacity=".9"/><stop offset="1" stop-color="#bfe8fb" stop-opacity=".4"/>
      </linearGradient>
    </defs>
    <rect width="1136" height="600" fill="url(#sky)"/>
    <path d="M0 150 C300 260 620 420 1136 560 L1136 600 C600 520 300 420 0 320 Z" fill="url(#band)" opacity=".55"/>
    <path d="M0 330 C320 430 700 560 1136 530 L1136 852 L0 852 Z" fill="#ffffff"/>
    <path d="M0 330 C320 420 650 540 1000 560 L1136 560 L1136 580 C800 590 400 510 0 400 Z" fill="#1d3a6e"/>
    <path d="M0 250 C300 360 620 480 1000 540 L1000 560 C620 520 300 420 0 330 Z" fill="#2aa6e0" opacity=".85"/>
    <path d="M0 405 C400 520 760 600 1136 520 L1136 548 C760 630 380 560 0 440 Z" fill="#7cc242"/>
    <path d="M0 440 C380 560 760 640 1136 548 L1136 575 C760 660 380 590 0 470 Z" fill="#cde9b8" opacity=".8"/>
    <circle cx="1030" cy="760" r="190" fill="#ffffff"/>
  </svg>
  <div role="img" aria-label="Photograph of a semi-submersible drilling rig lit at dusk at sea" style="position:absolute;left:660px;top:20px;width:476px;height:520px;border-radius:0 0 0 240px;background:linear-gradient(180deg,#3f8fd0 0%,#6aaede 45%,#314f7a 70%,#1f3b63 100%);"></div>
  <h1 class="cover-title">STRATEGIC REVIEW<b>2014</b></h1>
  <p class="cover-sub">Alex Rivera, 1 January 2014</p>
  <div class="brand brand--cover"><span class="mark"></span>NAVARA<small>MARINE SOLUTIONS</small></div>
</section>

<section class="slide slide--products">
  <svg class="art" viewBox="0 0 1136 852" aria-hidden="true">
    <path d="M0 680 L80 760 L0 770 Z" fill="#7cc242"/>
    <path d="M0 720 L70 760 L0 760 Z" fill="#cde9b8"/>
    <path d="M0 700 C150 760 330 820 450 852 L0 852 Z" fill="#5cc6f2" opacity=".5"/>
    <path d="M60 720 C200 780 320 830 380 852 L250 852 C180 810 110 770 60 720 Z" fill="#1fa3e0" opacity=".7"/>
    <path d="M0 760 C60 780 120 810 150 852 L0 852 Z" fill="#ffffff"/>
    <circle cx="1063" cy="255" r="112" fill="#fff"/>
    <circle cx="877" cy="461" r="86" fill="#fff"/>
    <circle cx="1018" cy="691" r="150" fill="#fff"/>
    <circle cx="760" cy="789" r="104" fill="#fff"/>
  </svg>
  <div role="img" aria-label="3D render of rig deck modules" style="position:absolute;left:956px;top:148px;width:214px;height:214px;border-radius:50%;background:radial-gradient(circle,#c9ccc8,#6d7170 70%,#2e3134)"></div>
  <div role="img" aria-label="Photograph of rig interior piping" style="position:absolute;left:797px;top:381px;width:160px;height:160px;border-radius:50%;background:radial-gradient(circle,#b5b7a6,#7a6f56 60%,#3c3a33)"></div>
  <div role="img" aria-label="Photograph of drill pipe racks on deck" style="position:absolute;left:876px;top:549px;width:284px;height:284px;border-radius:50%;background:radial-gradient(circle,#d8b88a,#a0835e 55%,#5a4f43)"></div>
  <div role="img" aria-label="3D render of a semi-submersible platform" style="position:absolute;left:662px;top:691px;width:196px;height:196px;border-radius:50%;background:linear-gradient(180deg,#d9dde0,#9aa2a6 60%,#6c767c)"></div>

  <header class="head"><h1>PRODUCTOS</h1><span class="tag">STRATEGIC REVIEW <b>2014</b></span></header>
  <h2 class="section-title products-title">Plataformas de <b>perforación semisumergibles</b></h2>
  <p class="dims">DIMENSIONES</p>

  <table class="specs specs--left">
    <tr><td>Largo total</td><td class="val">104,5 M</td></tr>
    <tr><td>Ancho total</td><td class="val">70,5 M</td></tr>
    <tr><td>Largo cubierta principal</td><td class="val">83,1 M</td></tr>
    <tr><td>Ancho cubierta principal</td><td class="val">69,5 M</td></tr>
    <tr><td>Helideck (diametro)</td><td class="val">27,75 M</td></tr>
    <tr><td>Moonpool dimensiones</td><td class="val">21,95 M X 7 M</td></tr>
    <tr><td>Calado</td><td class="val"></td></tr>
    <tr><td>Calado para operacion</td><td class="val">17,5 M</td></tr>
    <tr><td>Calado de supervivencia</td><td class="val">5,5 M</td></tr>
    <tr><td>Calado de transito</td><td class="val">9,75 M</td></tr>
    <tr><td>Desplacamiento</td><td class="val"></td></tr>
    <tr><td>Desplacamiento operativo</td><td class="val">40710 M.T.</td></tr>
    <tr><td>Desplacamiento de supervivencia</td><td class="val">38759 M.T.</td></tr>
    <tr><td>Desplasamiento en transito</td><td class="val">30830 M.T.</td></tr>
    <tr><td>Profundiad operacional</td><td class="val">100 – 1500 M.</td></tr>
    <tr><td>Capacidades de almacenaje</td><td class="val"></td></tr>
    <tr><td>Balastra de agua</td><td class="val">13000 M.</td></tr>
    <tr><td>Fcombustible</td><td class="val">3200 M.</td></tr>
  </table>

  <table class="specs specs--right">
    <tr><td>Agua de perforacion</td><td class="val">1360 M.</td></tr>
    <tr><td>Agua potable</td><td class="val">800 M.</td></tr>
    <tr><td>Lodos liquidos activos (superficie)</td><td class="val">750 M.</td></tr>
    <tr><td>Lodos liquidos de</td><td class="val">1170 M.</td></tr>
    <tr><td>Reserva(columna/pontón)</td><td class="val">400 M.</td></tr>
    <tr><td>Bentonita/barita en groso</td><td class="val">400 M.</td></tr>
    <tr><td>Cemento en groso</td><td class="val">1050 M.</td></tr>
    <tr><td>Aceite base</td><td class="val">1160 M.</td></tr>
    <tr><td>Salmuera</td><td class="val">350 M.</td></tr>
    <tr><td>Aguas negras</td><td class="val">5000 M.T.</td></tr>
    <tr><td>Carga variable</td><td class="val">10 KNOTS</td></tr>
    <tr><td>Velocidad de transito</td><td class="val"></td></tr>
  </table>

  <div class="brand brand--foot"><span class="mark"></span>NAVARA<small>MARINE SOLUTIONS</small></div>
</section>

<section class="slide slide--company">
  <svg class="art" viewBox="0 0 1136 852" aria-hidden="true">
    <path d="M0 680 L80 760 L0 770 Z" fill="#7cc242"/>
    <path d="M0 720 L70 760 L0 760 Z" fill="#cde9b8"/>
    <path d="M0 700 C150 760 330 820 450 852 L0 852 Z" fill="#5cc6f2" opacity=".5"/>
    <path d="M60 720 C200 780 320 830 380 852 L250 852 C180 810 110 770 60 720 Z" fill="#1fa3e0" opacity=".7"/>
    <path d="M0 760 C60 780 120 810 150 852 L0 852 Z" fill="#ffffff"/>
  </svg>
  <header class="head"><h1>NUESTRA EMPRESA</h1><span class="tag">STRATEGIC REVIEW <b>2014</b></span></header>
  <p class="lead">Está dedicada principalmente a brindar soluciones en el sector <b>marítimo petrolero, enfocándonos</b> en productos de vanguardia que se adapten a las necesidades en dicho sector.</p>
  <p class="body body--one">Buscamos la mejora continua de nuestros servicios, procesos y productos. Generamos sinergia de forma internacional, acercando a las grandes corporaciones y empresas de <b>CHINA,</b> facilitando los procesos de incorporación de éstas al mercado de exploración, producción, construcción, avituallamiento y mantenimiento marítimo del sector petrolero, en aguas profundas y cuencas del sureste del <b>GOLFO DE MÉXICO.</b></p>
  <div class="divider"></div>
  <h2 class="section-title company-title">Al estar posicionados en <b>Hong Kong y Beijing</b></h2>
  <p class="body body--two">Nos permite enlazar y trabajar con fabricantes y constructores que cubren las necesidades con estándares internacionales de calidad y garantía a satisfacción del sector marítimo petrolero, garantizando y fortaleciendo la orientación para nuestros clientes, en la gestión de las negociaciones y logrando que las operaciones sean seguras y confiables, maximizando así el valor de las oportunidades.</p>
  <div class="brand brand--foot"><span class="mark"></span>NAVARA<small>MARINE SOLUTIONS</small></div>
</section>

</body>
</html>
```